Medical device engineering service firm needs an update to flier

We do engineering design work for medical products, from ideation through injection-molded prototypes. Our clients have assay that needs automation, or an idea that needs to be made concrete. We have a 2-sided flier that needs an update to the look. This flier is mainly used as both a take away at trade shows to describe our services and provide our contact information.

```html
<!DOCTYPE html>
<html lang="en">
<head>
<meta charset="utf-8">
<title>Veridan Product Development – Two-Sided Flier</title>
<link rel="stylesheet" href="https://fonts.googleapis.com/css2?family=Montserrat:wght@400;500;600;700&family=Roboto:wght@500;700;900&display=swap">
<style>
:root{
  --purple:#6a2370;
  --purple-deep:#3d0d45;
  --purple-mid:#8b3a95;
  --green:#9fb84a;
  --green-light:#c6d67a;
  --ink:#2b2b2b;
  --text:#3a3a3a;
  --footer:#3b393a;
  --row-grey:#efefef;
  --line:#cfcfcf;
  --canvas:#ffffff;
}
*{box-sizing:border-box;margin:0;padding:0}
html,body{width:1200px;height:1200px;overflow:hidden;background:var(--canvas)}
body{position:relative;font-family:"Montserrat",Arial,sans-serif;color:var(--text)}
.page{position:absolute;top:261px;width:529px;height:679px;background:#fff;box-shadow:0 1px 6px rgba(0,0,0,.25);overflow:hidden}
.page--front{left:60px}
.page--back{left:611px}

/* brand name */
.brand{position:absolute;display:flex;align-items:center;gap:7px;color:var(--purple);font-weight:600;font-family:"Montserrat",Arial,sans-serif}
.brand__dot{width:14px;height:14px;border-radius:50%;background:var(--green)}
.brand__name{font-size:22px;line-height:1}
.brand__sub{display:block;font-size:7.5px;letter-spacing:.4px;margin-top:3px}

/* front header */
.hero{position:absolute;left:0;top:0;width:529px;height:290px}
.desk-scene{position:absolute;left:300px;top:182px;width:226px;height:205px;border-radius:50% 40% 12px 12px;background:radial-gradient(ellipse at 55% 45%,#5a5a66 0%,#2f2f38 45%,rgba(200,200,205,.6) 80%,rgba(255,255,255,0) 100%)}

.intro-title{position:absolute;left:30px;top:277px;font-size:12px;line-height:14.5px;color:var(--purple);font-weight:500}
.intro-title em{font-style:italic;font-weight:700;color:var(--ink)}
.intro-body{position:absolute;left:30px;top:313px;width:262px;font-size:8.2px;line-height:10.1px;color:var(--text)}
.statement{position:absolute;left:0;width:529px;top:396px;text-align:center;font-size:11.6px;line-height:14.5px;font-weight:600;color:#111}

.columns{position:absolute;left:31px;top:432px;width:464px;height:204px;display:flex;gap:4px}
.col{flex:1;border:1px solid var(--line);border-top:none;position:relative}
.col__head{background:var(--purple);color:#fff;font-family:"Roboto",Arial,sans-serif;font-weight:500;font-size:11.5px;height:22px;line-height:22px;text-align:center;border-radius:3px 3px 0 0}
.col ul{list-style:none;padding:4px 4px 0 6px}
.col li{position:relative;padding-left:10px;font-size:8.1px;line-height:9.3px;margin-bottom:5.6px;color:var(--text)}
.col li::before{content:"";position:absolute;left:0;top:2.5px;width:4px;height:4px;border-radius:50%;border:1.2px solid var(--green)}

/* footer */
.footer{position:absolute;left:0;bottom:0;width:529px;height:37px;background:var(--footer);color:#fff}
.footer__phone{position:absolute;left:0;top:0;width:200px;height:37px;background:var(--purple);border-radius:0 60px 0 0 / 0 37px 0 0;display:flex;align-items:center;padding-left:32px;font-size:12px;letter-spacing:.2px}
.footer__item{position:absolute;top:0;height:37px;display:flex;align-items:center;gap:7px;font-size:8.6px}
.footer__mail{left:219px}
.footer__web{left:378px}
.icon{flex:none}
.footer__phone .icon{position:absolute;left:32px}
.footer__phone span{margin-left:20px}

/* back */
.steps-title{position:absolute;right:37px;top:36px;text-align:right;font-family:"Roboto",Arial,sans-serif}
.steps-title h1{font-size:29px;line-height:30px;font-weight:900;color:var(--purple);letter-spacing:.6px}
.steps-title h2{font-size:14px;font-weight:500;color:var(--green);letter-spacing:.3px;margin-top:1px}

.phase{position:absolute;border:1px solid var(--line);background:#fff}
.phase--grey{background:var(--row-grey)}
.phase__tab{position:absolute;left:0;top:0;bottom:0;width:28px;display:flex;align-items:center;justify-content:center}
.phase__tab--purple{background:var(--purple)}
.phase__tab--green{background:var(--green)}
.phase__tab span{transform:rotate(-90deg);white-space:nowrap;color:#fff;font-family:"Roboto",Arial,sans-serif;font-weight:700;font-size:11px;letter-spacing:.5px}
.phase__cells{position:absolute;left:28px;right:0;top:0;bottom:0;display:flex}
.step{flex:1;display:flex;flex-direction:column;align-items:center;padding-top:18px}
.step__art{width:50px;height:50px;border-radius:6px}
.step p{margin-top:18px;font-size:7.4px;line-height:8.9px;text-align:center;color:var(--text);padding:0 6px}
.art--red{background:radial-gradient(circle,#e84a3a 0 40%,#b7221b 70%,rgba(255,255,255,0) 72%)}
.art--blue{background:linear-gradient(180deg,#c9d6e6,#3c6fb3 70%,#d8dde4)}
.art--mono{background:linear-gradient(180deg,#e9e9e9,#555 90%)}
.art--desk{background:linear-gradient(180deg,#d97a2c,#333 55%,#7a4a2a)}
.art--grey{background:linear-gradient(180deg,#f3f3f3,#b9bcc2)}
.art--cycle{border-radius:50%;background:radial-gradient(circle,#2bb0c8 0 45%,#0f4c6b 70%,rgba(255,255,255,0) 72%)}
.art--teal{background:linear-gradient(135deg,#5fb5a6,#dfe8e4 60%,#6b8e86)}
.art--gold{background:linear-gradient(135deg,#d8c48a,#8a7d6b 60%,#c8b27a)}
.art--glove{background:linear-gradient(135deg,#9fb6d4,#e8eef5 60%,#6d86a8)}
.art--docs{background:linear-gradient(180deg,#f1e6a6,#6a7c3a 70%,#e5e0cf)}

.company{position:absolute;left:33px;top:606px}
.company strong{display:block;color:var(--purple);font-size:11px;font-weight:700}
.company span{display:block;font-size:10.4px;color:var(--ink);margin-top:1px}
.cert-badge{position:absolute;left:446px;top:600px;width:34px;height:34px;border-radius:50%;background:#2a6fb5}
</style>
</head>
<body>

<!-- FRONT -->
<section class="page page--front">
  <svg class="hero" viewBox="0 0 529 290" role="img" aria-label="Technical line drawings of medical devices, instruments and lab equipment on a purple background">
    <defs>
      <radialGradient id="heroGlow" cx="62%" cy="38%" r="70%">
        <stop offset="0" stop-color="#b66ec0"/>
        <stop offset=".45" stop-color="#7a2e86"/>
        <stop offset="1" stop-color="#240827"/>
      </radialGradient>
    </defs>
    <path d="M0,106 C150,100 290,60 330,0 L529,0 L529,258 C380,250 180,250 0,266 Z" fill="url(#heroGlow)"/>
    <path d="M0,102 C150,96 290,56 326,0 L336,0 C296,62 152,108 0,112 Z" fill="#6a2370"/>
    <path d="M0,266 C180,250 380,250 529,258 L529,266 C380,258 180,258 0,274 Z" fill="#9fb84a"/>
  </svg>

  <div class="brand" style="left:45px;top:40px">
    <div>
      <span class="brand__name">veridan</span>
      <span class="brand__sub">PRODUCT DEVELOPMENT</span>
    </div>
    <span class="brand__dot"></span>
  </div>

  <div class="desk-scene" role="img" aria-label="Photo of an engineer working at a computer desk"></div>

  <h2 class="intro-title"><em>Rapid</em> Engineering Design of Medical Devices<br>Specializing in Plastics</h2>
  <p class="intro-body">Our highly experienced biomedical &amp; mechanical engineers leverage our extensive in-house fabrication capabilities to create proven, manufacturable designs with unmatched speed, efficiency and quality. They have developed over 300 successful designs, forming our deep portfolio that has generated hundreds of millions of dollars for our clients. It includes FDA Class I, II &amp; III devices, developed under our ISO 13485 certified quality management system.</p>

  <p class="statement">We specialize in engineering design and design-for-manufacturing<br>of innovative medical and life science devices that use plastics</p>

  <div class="columns">
    <div class="col">
      <div class="col__head">Our Services Include:</div>
      <ul>
        <li>Concept Development</li>
        <li>Engineering and Design</li>
        <li>Industrial Design</li>
        <li>Design for Manufacturing and Assembly</li>
        <li>Design Control per ISO 13485</li>
        <li>Finite Element Analysis (FEA)</li>
        <li>Design Verification Testing</li>
        <li>Test Method Development</li>
        <li>Test and Assembly Fixture development</li>
        <li>Transfer to Manufacturing</li>
      </ul>
    </div>
    <div class="col">
      <div class="col__head">Our In-House Capabilities:</div>
      <ul>
        <li>Stereolithography (SLA) Prototyping</li>
        <li>CNC Machining / Fabrication</li>
        <li>Prototype Mold Fabrication</li>
        <li>Prototype Injection Molding</li>
        <li>Prototype Liquid Injection Molding (LIM) of Silicone</li>
        <li>Clean Room Assembly</li>
        <li>Product Reliability Testing</li>
        <li>Plastics Assembly Expertise</li>
        <li>Material Selection Expertise, Research and Testing</li>
        <li>Low Volume Manufacturing</li>
      </ul>
    </div>
    <div class="col">
      <div class="col__head">Our Portfolio Includes:</div>
      <ul>
        <li>Diagnostics / Molecular Diagnostics</li>
        <li>Sample Collection/Preparation</li>
        <li>Life Science / Laboratory Products</li>
        <li>Microfluidics/ SmallVolume Handling</li>
        <li>Buffer &amp; Reagent Storage &amp; Delivery</li>
        <li>Surgical / Clinical Tools</li>
        <li>Drug Delivery Devices</li>
        <li>Electromechanical Devices</li>
        <li>Point-of-Care and Home Use Devices</li>
      </ul>
    </div>
  </div>

  <footer class="footer">
    <div class="footer__phone">
      <svg class="icon" width="15" height="15" viewBox="0 0 16 16"><circle cx="8" cy="8" r="7" fill="none" stroke="#c6d67a" stroke-width="1.2"/><path d="M5.2 4.3l1.3-.3.9 2-.8.7c.4.9 1 1.5 1.9 1.9l.7-.8 2 .9-.3 1.3c-3.3.2-5.9-2.4-5.7-5.7z" fill="#c6d67a"/></svg>
      <span>+ 1 555 014 2270 x 2</span>
    </div>
    <div class="footer__item footer__mail">
      <svg class="icon" width="12" height="9" viewBox="0 0 12 9"><rect x=".5" y=".5" width="11" height="8" fill="#9fb84a"/><path d="M.5.5L6 5 11.5.5" fill="none" stroke="#3b393a" stroke-width="1"/></svg>
      <span>contact@veridanpd.com</span>
    </div>
    <div class="footer__item footer__web">
      <svg class="icon" width="11" height="11" viewBox="0 0 12 12"><g fill="none" stroke="#9fb84a" stroke-width="1"><circle cx="6" cy="6" r="5"/><ellipse cx="6" cy="6" rx="2.2" ry="5"/><path d="M1 6h10M2 3.3h8M2 8.7h8"/></g></svg>
      <span>www.veridanpd.com</span>
    </div>
  </footer>
</section>

<!-- BACK -->
<section class="page page--back">
  <div class="brand" style="left:47px;top:48px">
    <div>
      <span class="brand__name">veridan</span>
      <span class="brand__sub">PRODUCT DEVELOPMENT</span>
    </div>
    <span class="brand__dot"></span>
  </div>

  <div class="steps-title">
    <h1>STEPS TO SUCCESS</h1>
    <h2>OUR MEDICAL DEVELOPMENT PROCESS</h2>
  </div>

  <div class="phase" style="left:33px;top:95px;width:463px;height:119px">
    <div class="phase__tab phase__tab--purple"><span>PHASE 1</span></div>
    <div class="phase__cells">
      <div class="step"><div class="step__art art--red" role="img" aria-label="Target icon"></div><p>Define the product requirements, giving us a well-defined target for development.</p></div>
      <div class="step"><div class="step__art art--blue" role="img" aria-label="Lab flasks and sample tubes"></div><p>Develop concepts that provide an array of potential design solutions.</p></div>
      <div class="step"><div class="step__art art--mono" role="img" aria-label="Presenter beside a flowchart board"></div><p>Analyze and present concepts. Determine which one best meets all product requirements.</p></div>
    </div>
  </div>

  <div class="phase phase--grey" style="left:33px;top:222px;width:463px;height:117px">
    <div class="phase__tab phase__tab--green"><span>PHASE 2</span></div>
    <div class="phase__cells">
      <div class="step"><div class="step__art art--desk" role="img" aria-label="Engineer at a computer workstation"></div><p>Develop a detailed model of the selected concept in 3D CAD.</p></div>
      <div class="step"><div class="step__art art--grey" role="img" aria-label="Rapid prototype part"></div><p>Fabricate and test rapid prototype against product requirements.</p></div>
      <div class="step"><div class="step__art art--cycle" role="img" aria-label="Iteration cycle icon"></div><p>Iterate the design until it meets requirements.</p></div>
    </div>
  </div>

  <div class="phase" style="left:33px;top:346px;width:463px;height:119px">
    <div class="phase__tab phase__tab--purple"><span>PHASE 3</span></div>
    <div class="phase__cells">
      <div class="step"><div class="step__art art--teal" role="img" aria-label="Prototype tooling machine"></div><p>Fabricate prototype tooling in-house that we can easily iterate as needed.</p></div>
      <div class="step"><div class="step__art art--gold" role="img" aria-label="Injection mold halves"></div><p>Mold and assemble fully functional, production quality devices.</p></div>
      <div class="step"><div class="step__art art--cycle" role="img" aria-label="Iteration cycle icon"></div><p>Iterate the mold &amp; assembly until it meets requirements.</p></div>
    </div>
  </div>

  <div class="phase phase--grey" style="left:33px;top:473px;width:163px;height:119px">
    <div class="phase__tab phase__tab--green"><span>PHASE 4</span></div>
    <div class="phase__cells">
      <div class="step"><div class="step__art art--glove" role="img" aria-label="Gloved hand holding a test device"></div><p>Perform Design Verification Testing to confirm that all designs requirements are met.</p></div>
    </div>
  </div>

  <div class="phase" style="left:200px;top:473px;width:296px;height:119px">
    <div class="phase__tab phase__tab--purple"><span>PHASE 5</span></div>
    <div class="phase__cells">
      <div class="step"><div class="step__art art--docs" role="img" aria-label="Clipboard with factory icon"></div><p>Seamlessly transfer to manufacturing.</p></div>
      <div class="step"><div class="step__art art--docs" role="img" aria-label="Patent certificate and documents"></div><p>Support patent and regulatory approval processes.</p></div>
    </div>
  </div>

  <div class="company">
    <strong>Veridan Product Development</strong>
    <span>1480 Harbor View Rd. Oceanside, CA 92054</span>
  </div>
  <div class="cert-badge" role="img" aria-label="Quality certification badge"></div>

  <footer class="footer">
    <div class="footer__phone">
      <svg class="icon" width="15" height="15" viewBox="0 0 16 16"><circle cx="8" cy="8" r="7" fill="none" stroke="#c6d67a" stroke-width="1.2"/><path d="M5.2 4.3l1.3-.3.9 2-.8.7c.4.9 1 1.5 1.9 1.9l.7-.8 2 .9-.3 1.3c-3.3.2-5.9-2.4-5.7-5.7z" fill="#c6d67a"/></svg>
      <span>+ 1 555 014 2270 x 2</span>
    </div>
    <div class="footer__item footer__mail">
      <svg class="icon" width="12" height="9" viewBox="0 0 12 9"><rect x=".5" y=".5" width="11" height="8" fill="#9fb84a"/><path d="M.5.5L6 5 11.5.5" fill="none" stroke="#3b393a" stroke-width="1"/></svg>
      <span>contact@veridanpd.com</span>
    </div>
    <div class="footer__item footer__web">
      <svg class="icon" width="11" height="11" viewBox="0 0 12 12"><g fill="none" stroke="#9fb84a" stroke-width="1"><circle cx="6" cy="6" r="5"/><ellipse cx="6" cy="6" rx="2.2" ry="5"/><path d="M1 6h10M2 3.3h8M2 8.7h8"/></g></svg>
      <span>www.veridanpd.com</span>
    </div>
  </footer>
</section>

</body>
</html>
```